Business Card Design Project

I want a cleaner business card and envelope then what we have now, its too crowded.
Updates

I update with logo, this can be changed anyway you feel it looks best. I also have put gaurantee on there and extended time, this is my first time doing this. Also gave an example of current card

Target Market(s)

a wide array of customers from lattice 700 to small companies and cleints

Industry/Entity Type

Business

Requirements
Must have
• Need to have address, telephone number email
Nice to have
• a sharp professional card that stands out but is still very clean.
Should not have
• Not crazy looking

```html
<!DOCTYPE html>
<html lang="en">
<head>
<meta charset="utf-8">
<title>Alder Insurance Group – Stationery Options</title>
<link rel="stylesheet" href="https://fonts.googleapis.com/css2?family=Source+Sans+3:wght@400;600;700&family=Crimson+Text:ital,wght@1,700&display=swap">
<style>
  :root {
    --backdrop: #ece9e4;
    --paper: #ffffff;
    --ink: #2b2b2b;
    --brand-grey: #4a4a4c;
    --rule: #8d8e92;
    --flap-light: #b9babd;
    --label-bg: #8a8178;
  }
  * { box-sizing: border-box; margin: 0; padding: 0; }
  html, body { width: 1057px; height: 1200px; overflow: hidden; }
  body {
    position: relative;
    background: var(--backdrop);
    font-family: "Source Sans 3", Arial, sans-serif;
    color: var(--ink);
  }
  .option-label {
    position: absolute;
    left: 0; width: 1057px;
    text-align: center;
    font-weight: 700;
    font-size: 17px;
    letter-spacing: 0.5px;
    color: var(--label-bg);
  }
  .card {
    position: absolute;
    width: 433px; height: 248px;
    background: var(--paper);
    border-radius: 18px;
    box-shadow: 0 2px 6px rgba(0,0,0,0.18);
    overflow: hidden;
  }
  .double-rule {
    position: absolute;
    left: 0; right: 0;
    height: 8px;
    border-top: 2px solid var(--rule);
    border-bottom: 2px solid var(--rule);
  }
  .card .double-rule { top: 210px; }
  .brand {
    position: absolute;
    left: 0; right: 0;
    text-align: center;
    color: var(--brand-grey);
    font-weight: 400;
  }
  .brand-square {
    display: block;
    margin: 0 auto 10px;
    width: 66px; height: 66px;
    background: var(--brand-grey);
  }
  .brand-name {
    display: block;
    font-size: 26px;
    letter-spacing: 6px;
    line-height: 1;
  }
  .brand-tag {
    display: block;
    font-size: 12.5px;
    letter-spacing: 2.2px;
    line-height: 1.3;
  }
  .holder-name {
    position: absolute;
    left: 0; right: 0;
    text-align: center;
    font-family: "Crimson Text", Georgia, serif;
    font-style: italic;
    font-weight: 700;
    font-size: 16px;
  }
  .contact {
    position: absolute;
    left: 0; right: 0;
    text-align: center;
    font-size: 11px;
    line-height: 15px;
  }
  .contact .gap { height: 12px; }
  .contact .gap-wide { height: 20px; }
  .icon { width: 10px; height: 9px; vertical-align: -1px; margin-right: 3px; }
  .envelope {
    position: absolute;
    left: 161px; top: 743px;
    width: 738px; height: 407px;
  }
  .envelope-flap { position: absolute; left: 0; top: 0; }
  .flap-square {
    position: absolute;
    left: 361px; top: 30px;
    width: 32px; height: 32px;
    background: var(--flap-light);
    box-shadow: 0 1px 2px rgba(0,0,0,0.25);
  }
  .envelope-body {
    position: absolute;
    left: 0; top: 86px;
    width: 738px; height: 321px;
    background: var(--paper);
    box-shadow: 0 2px 6px rgba(0,0,0,0.18);
  }
  .envelope-body .brand { left: 40px; right: auto; top: 38px; width: 154px; }
  .envelope-body .double-rule { top: 277px; }
  .envelope-return {
    position: absolute;
    left: 36px; top: 253px;
    font-size: 11px;
  }
</style>
</head>
<body>
  <svg width="0" height="0" style="position:absolute">
    <defs>
      <symbol id="icon-phone" viewBox="0 0 10 10"><path d="M2 0.5 L3.6 0.5 L4.2 2.8 L3 3.6 Q4 6 6.4 7 L7.2 5.8 L9.5 6.4 L9.5 8 Q9.5 9.5 8 9.5 Q0.5 8.5 0.5 2 Q0.5 0.5 2 0.5 Z" fill="#555"/></symbol>
      <symbol id="icon-mail" viewBox="0 0 12 9"><rect x="0.5" y="0.5" width="11" height="8" fill="none" stroke="#555"/><path d="M0.5 0.5 L6 5 L11.5 0.5" fill="none" stroke="#555"/></symbol>
      <symbol id="icon-fax" viewBox="0 0 12 9"><rect x="3" y="0.5" width="6" height="3" fill="#555"/><rect x="0.5" y="3.5" width="11" height="5" fill="#555"/></symbol>
      <symbol id="icon-globe" viewBox="0 0 10 10"><circle cx="5" cy="5" r="4.4" fill="none" stroke="#555"/><ellipse cx="5" cy="5" rx="2" ry="4.4" fill="none" stroke="#555"/><path d="M0.6 5 H9.4" stroke="#555"/></symbol>
      <linearGradient id="flap-shade" x1="0" x2="1" y1="0" y2="0">
        <stop offset="0" stop-color="#5b5c5f"/>
        <stop offset="0.5" stop-color="#a9aaad"/>
        <stop offset="1" stop-color="#5b5c5f"/>
      </linearGradient>
    </defs>
  </svg>

  <div class="option-label" style="top:36px">OPTION - 1</div>

  <section class="card" style="left:59px; top:78px">
    <div class="brand" style="top:56px">
      <span class="brand-square"></span>
      <span class="brand-name">ALDER</span>
      <span class="brand-tag">INSURANCE GROUP</span>
    </div>
    <div class="double-rule"></div>
  </section>

  <section class="card" style="left:548px; top:83px">
    <div class="contact" style="top:94px">
      <div><svg class="icon"><use href="#icon-phone"/></svg>555 - 214 - 3800 (ext. 418) / &nbsp;555 - 407 - 2291 (Direct)</div>
      <div><svg class="icon"><use href="#icon-mail"/></svg>mquinn-hollis@alderagency.com</div>
      <div class="gap"></div>
      <div>18230 Orchard Row; Maple Ridge, OH 44021</div>
    </div>
    <div class="double-rule"></div>
  </section>

  <div class="option-label" style="top:358px">OPTION - 2</div>

  <section class="card" style="left:71px; top:402px">
    <div class="brand" style="top:44px">
      <span class="brand-square" style="width:58px;height:58px"></span>
      <span class="brand-name" style="font-size:23px">ALDER</span>
      <span class="brand-tag" style="font-size:11.5px">INSURANCE GROUP</span>
    </div>
    <div class="holder-name" style="top:158px">Marla Quinn - Hollis</div>
    <div class="double-rule"></div>
  </section>

  <section class="card" style="left:561px; top:407px">
    <div class="contact" style="top:62px">
      <div><svg class="icon"><use href="#icon-phone"/></svg>555 - 214 - 3800 (ext. 418) / &nbsp;555 - 407 - 2291 (Direct)</div>
      <div><svg class="icon"><use href="#icon-fax"/></svg>555 - 214 - 3803</div>
      <div class="gap"></div>
      <div><svg class="icon"><use href="#icon-mail"/></svg>mquinn-hollis@alderagency.com</div>
      <div><svg class="icon"><use href="#icon-globe"/></svg>www.alderagency.com</div>
      <div class="gap-wide"></div>
      <div>18230 Orchard Row; Maple Ridge, OH 44021</div>
    </div>
    <div class="double-rule"></div>
  </section>

  <section class="envelope">
    <svg class="envelope-flap" width="738" height="88" viewBox="0 0 738 88">
      <path d="M0 87 L52 18 Q66 0 90 0 L648 0 Q672 0 686 18 L738 87 Z" fill="url(#flap-shade)"/>
    </svg>
    <div class="flap-square"></div>
    <div class="envelope-body">
      <div class="brand">
        <span class="brand-square" style="width:58px;height:58px"></span>
        <span class="brand-name" style="font-size:22px">ALDER</span>
        <span class="brand-tag" style="font-size:11.5px">INSURANCE GROUP</span>
      </div>
      <div class="envelope-return">18230 Orchard Row; Maple Ridge, OH 44021 &nbsp;<svg class="icon"><use href="#icon-mail"/></svg>mquinn-hollis@alderagency.com</div>
      <div class="double-rule"></div>
    </div>
  </section>
</body>
</html>
```